Automotive eCommerce Business looking for a business card design

Looking for a clean and simple business card design. Our company name is "Tundra Motors" and we are a company specializing in the ecommerce sales of automotive parts, specifically for pick up trucks and large SUVs. Our company colours are red, black, and white.

Feel free to use the logo provided or create a new logo that you seem fit. Looking forward to your creative ideas!

Industry/Entity Type

Automotive

Contact Information for Business Card

We were thinking of a possibly two-sided design featuring just the logo and company name on one side, and personal information on the other side. Single sided designs will be considered as well.

Font styles to use
Serif
Sans Serif
Decorative

Colors
ec1f27
ffffff
000000

Requirements
Must have
• Space for employee's name, title, phone number and email address, along with the company address and website somewhere.

```html
<!DOCTYPE html>
<html lang="en">
<head>
<meta charset="utf-8">
<title>Tundra Motors – Business Card</title>
<link href="https://fonts.googleapis.com/css2?family=Roboto:wght@400;500;700&display=swap" rel="stylesheet">
<style>
  :root {
    --backdrop: #e6e4e1;
    --card: #f7f7f6;
    --brand-red: #a11d22;
    --ink: #4a4a4a;
    --ink-soft: #5c5c5c;
    --rule: #8a8a8a;
    --band-grey: #4d4f51;
  }
  * { margin: 0; padding: 0; box-sizing: border-box; }
  html, body {
    width: 1200px; height: 960px; overflow: hidden;
    background: var(--backdrop);
    font-family: "Roboto", Arial, sans-serif;
  }
  .stage { position: relative; width: 1200px; height: 960px; }

  .card {
    position: absolute;
    width: 600px; height: 345px;
    background: var(--card);
    border-radius: 16px;
    overflow: hidden;
    box-shadow: 0 2px 6px rgba(0,0,0,.18);
  }
  .card--front { left: 320px; top: 97px; }
  .card--back  { left: 320px; top: 492px; }

  /* front face */
  .front-mark {
    position: absolute; left: 247px; top: 80px;
    width: 106px; height: 106px;
    background: var(--brand-red);
  }
  .front-name {
    position: absolute; left: 0; right: 0; top: 242px;
    text-align: center;
    font-size: 27px; font-weight: 500; letter-spacing: 1px;
    color: var(--ink-soft);
  }
  .front-web {
    position: absolute; left: 0; right: 0; top: 302px;
    text-align: center;
    font-size: 14px; letter-spacing: 4px;
    color: var(--ink);
  }

  /* back face */
  .back-mark {
    position: absolute; left: 468px; top: 44px;
    width: 80px; height: 80px;
    background: var(--brand-red);
  }
  .back-name {
    position: absolute; right: 42px; top: 154px;
    font-size: 19px; font-weight: 500;
    color: var(--ink-soft);
  }
  .person {
    position: absolute; left: 29px; top: 192px;
  }
  .person__name {
    font-size: 20px; font-weight: 700; color: var(--brand-red);
    line-height: 24px;
  }
  .person__title {
    font-size: 15px; font-weight: 500; color: var(--ink);
    line-height: 20px; letter-spacing: .2px;
  }
  .divider {
    position: absolute; left: 29px; top: 242px;
    width: 528px; height: 1px; background: var(--rule);
  }
  .contacts {
    position: absolute; left: 29px; top: 252px;
    list-style: none;
    font-size: 14px; color: var(--ink); line-height: 19.5px;
  }
  .contacts li { display: flex; align-items: center; gap: 8px; }
  .contacts svg { width: 14px; height: 14px; fill: var(--brand-red); flex: none; }
  .address {
    position: absolute; right: 42px; top: 252px;
    text-align: right; font-style: normal;
    font-size: 14px; color: var(--ink); line-height: 18px;
  }
  .footer-band {
    position: absolute; left: 0; bottom: 0; width: 100%; height: 13px;
  }
</style>
</head>
<body>
<main class="stage">

  <section class="card card--front" aria-label="Card front">
    <div class="front-mark" aria-hidden="true"></div>
    <div class="front-name">Tundra Motors</div>
    <div class="front-web">www.tundramotors.com</div>
  </section>

  <section class="card card--back" aria-label="Card back">
    <div class="back-mark" aria-hidden="true"></div>
    <div class="back-name">Tundra Motors</div>

    <div class="person">
      <div class="person__name">MARA OKAFOR</div>
      <div class="person__title">PRODUCT DEVELOPMENT MANAGER</div>
    </div>
    <div class="divider"></div>

    <ul class="contacts">
      <li>
        <svg viewBox="0 0 24 24" aria-hidden="true"><path d="M6.6 10.8a15.1 15.1 0 0 0 6.6 6.6l2.2-2.2c.3-.3.7-.4 1-.2 1.1.4 2.3.6 3.6.6.6 0 1 .4 1 1V20c0 .6-.4 1-1 1C10.6 21 3 13.4 3 4c0-.6.4-1 1-1h3.5c.6 0 1 .4 1 1 0 1.3.2 2.5.6 3.6.1.3 0 .7-.2 1z"/></svg>
        1 (555) 014-0192
      </li>
      <li>
        <svg viewBox="0 0 24 24" aria-hidden="true"><path d="M7 1h10a2 2 0 0 1 2 2v18a2 2 0 0 1-2 2H7a2 2 0 0 1-2-2V3a2 2 0 0 1 2-2zm0 3v14h10V4zm5 15.5a1.2 1.2 0 1 0 0 2.4 1.2 1.2 0 0 0 0-2.4z"/></svg>
        1 (555) 017-3348
      </li>
      <li>
        <svg viewBox="0 0 24 24" aria-hidden="true"><path d="M2 5h20v2.2l-10 6.3L2 7.2zm0 4.6 10 6.3 10-6.3V19H2z"/></svg>
        mara@tundramotors.com
      </li>
    </ul>

    <address class="address">
      Unit 4120, 88 Alder Street<br>
      Brookvale, WA 98000<br>
      www.tundramotors.com
    </address>

    <svg class="footer-band" viewBox="0 0 600 13" preserveAspectRatio="none" aria-hidden="true">
      <polygon points="0,0 392,0 388,13 0,13" fill="var(--brand-red)"/>
      <polygon points="397,0 600,0 600,13 393,13" fill="var(--band-grey)"/>
    </svg>
  </section>

</main>
</body>
</html>
```